Sticker Design for Company Equipment - Velunora

We are looking for a professional and clean graphic design for a set of stickers to apply on our company equipment (cleaning, gardening, pest control). The stickers must include our logo (the square with the three colored segments and the checkmark), our phone number, email address, and website, you can decide to use all three or just our website based on your graphic needs. It is important that it has an attractive sharp and clear look. The design should be consistent with our brand identity and give a polished, trustworthy look to our tools and machinery. We need a modular design that works in different formats (rectangular, square, round), depending on the type of equipment.

Need extra days to review

```html
<!DOCTYPE html>
<html lang="en">
<head>
<meta charset="utf-8">
<title>Velunora – Equipment Sticker Set</title>
<link rel="stylesheet" href="https://fonts.googleapis.com/css2?family=Montserrat:wght@500;700&family=Lato:wght@400;700&display=swap">
<style>
  :root{
    --navy:#231f60;
    --green:#76bd43;
    --orange:#f26b21;
    --paper:#ffffff;
    --backdrop:#e6e7e9;
    --shadow:rgba(0,0,0,.18);
  }
  *{box-sizing:border-box;margin:0;padding:0}
  html,body{width:1200px;height:501px;overflow:hidden;background:var(--backdrop)}
  .canvas{position:relative;width:1200px;height:501px}

  .sticker{position:absolute;background:var(--paper);color:var(--navy);box-shadow:3px 3px 3px var(--shadow)}
  .sticker-frame{position:absolute;border:2px solid var(--navy);border-radius:4px}
  .sticker-rect{left:148px;top:157px;width:318px;height:186px}
  .sticker-rect .sticker-frame{inset:6px}
  .sticker-square{left:598px;top:157px;width:187px;height:186px}
  .sticker-square .sticker-frame{inset:5px}
  .sticker-round{left:895px;top:172px;width:157px;height:157px;border-radius:50%}
  .sticker-round .sticker-frame{inset:3px;border-radius:50%}

  .mark{position:absolute;left:50%;transform:translateX(-50%);background:var(--navy)}

  .line{position:absolute;left:0;right:0;text-align:center;transform:translateY(-50%);white-space:nowrap;line-height:1}

  .brand-name{font-family:"Montserrat",sans-serif;font-weight:700;color:var(--navy);letter-spacing:.02em}

  .services{font-family:"Montserrat",sans-serif;font-weight:500;letter-spacing:.1em}
  .service-cleaning{color:var(--navy)}
  .service-gardening{color:var(--green)}
  .service-pest{color:var(--orange)}

  .rule{position:absolute;left:50%;transform:translateX(-50%);height:2px;
    background:linear-gradient(90deg,var(--navy) 0 33.3%,var(--green) 33.3% 66.6%,var(--orange) 66.6%)}

  .contact{font-family:"Lato",sans-serif;font-weight:400;color:var(--navy)}
  .contact-item{display:inline-flex;align-items:center;gap:.15em}
  .contact-item + .contact-item{margin-left:.45em}
  .icon{width:1em;height:1em;fill:none;stroke:var(--navy)}
  .icon-phone{fill:var(--navy);stroke:none}
  .icon-at{font-weight:700;font-size:1.1em}
</style>
</head>
<body>
<main class="canvas">

  <!-- Rectangular sticker -->
  <section class="sticker sticker-rect" aria-label="Rectangular sticker">
    <div class="sticker-frame"></div>
    <div class="mark" style="top:23px;width:56px;height:56px"></div>
    <div class="line brand-name" style="top:101px;font-size:40px">Velunora</div>
    <div class="line services" style="top:124px;font-size:9.5px"><span class="service-cleaning">CLEANING</span><span class="service-gardening">·GARDENING</span><span class="service-pest">·PESTCONTROL</span></div>
    <div class="rule" style="top:135px;width:195px"></div>
    <div class="line contact" style="top:147px;font-size:11px">
      <span class="contact-item"><svg class="icon icon-phone" viewBox="0 0 24 24"><path d="M6.6 10.8a15.1 15.1 0 0 0 6.6 6.6l2.2-2.2c.3-.3.7-.4 1-.2 1.1.4 2.3.6 3.6.6.6 0 1 .4 1 1V20c0 .6-.4 1-1 1A17 17 0 0 1 3 4c0-.6.4-1 1-1h3.5c.6 0 1 .4 1 1 0 1.3.2 2.5.6 3.6.1.3 0 .7-.2 1z"/></svg>+39 320 5550174</span>
    </div>
    <div class="line contact" style="top:160px;font-size:11px">
      <span class="contact-item"><svg class="icon" viewBox="0 0 24 24" stroke-width="2"><circle cx="12" cy="12" r="9"/><path d="M3 12h18M12 3c3 3 3 15 0 18M12 3c-3 3-3 15 0 18"/></svg>Velunora.srl</span>
      <span class="contact-item"><span class="icon-at">@</span>office@velunora.srl</span>
    </div>
  </section>

  <!-- Square sticker -->
  <section class="sticker sticker-square" aria-label="Square sticker">
    <div class="sticker-frame"></div>
    <div class="mark" style="top:20px;width:55px;height:55px"></div>
    <div class="line brand-name" style="top:94px;font-size:27px">Velunora</div>
    <div class="line services" style="top:109px;font-size:6.4px"><span class="service-cleaning">CLEANING</span><span class="service-gardening">·GARDENING</span><span class="service-pest">·PESTCONTROL</span></div>
    <div class="rule" style="top:123px;width:146px"></div>
    <div class="line contact" style="top:138px;font-size:12px">
      <span class="contact-item"><svg class="icon icon-phone" viewBox="0 0 24 24"><path d="M6.6 10.8a15.1 15.1 0 0 0 6.6 6.6l2.2-2.2c.3-.3.7-.4 1-.2 1.1.4 2.3.6 3.6.6.6 0 1 .4 1 1V20c0 .6-.4 1-1 1A17 17 0 0 1 3 4c0-.6.4-1 1-1h3.5c.6 0 1 .4 1 1 0 1.3.2 2.5.6 3.6.1.3 0 .7-.2 1z"/></svg>+39 320 5550174</span>
    </div>
    <div class="line contact" style="top:153px;font-size:12px">
      <span class="contact-item"><svg class="icon" viewBox="0 0 24 24" stroke-width="2"><circle cx="12" cy="12" r="9"/><path d="M3 12h18M12 3c3 3 3 15 0 18M12 3c-3 3-3 15 0 18"/></svg>Velunora.srl</span>
    </div>
    <div class="line contact" style="top:166px;font-size:12px">
      <span class="contact-item"><span class="icon-at">@</span>office@velunora.srl</span>
    </div>
  </section>

  <!-- Round sticker -->
  <section class="sticker sticker-round" aria-label="Round sticker">
    <div class="sticker-frame"></div>
    <div class="mark" style="top:13px;width:43px;height:43px"></div>
    <div class="line brand-name" style="top:72px;font-size:21px">Velunora</div>
    <div class="line services" style="top:84px;font-size:5.1px"><span class="service-cleaning">CLEANING</span><span class="service-gardening">·GARDENING</span><span class="service-pest">·PESTCONTROL</span></div>
    <div class="rule" style="top:95px;width:116px;height:1.5px"></div>
    <div class="line contact" style="top:105px;font-size:9px">
      <span class="contact-item"><svg class="icon icon-phone" viewBox="0 0 24 24"><path d="M6.6 10.8a15.1 15.1 0 0 0 6.6 6.6l2.2-2.2c.3-.3.7-.4 1-.2 1.1.4 2.3.6 3.6.6.6 0 1 .4 1 1V20c0 .6-.4 1-1 1A17 17 0 0 1 3 4c0-.6.4-1 1-1h3.5c.6 0 1 .4 1 1 0 1.3.2 2.5.6 3.6.1.3 0 .7-.2 1z"/></svg>+39 320 5550174</span>
    </div>
    <div class="line contact" style="top:116px;font-size:9px">
      <span class="contact-item"><svg class="icon" viewBox="0 0 24 24" stroke-width="2"><circle cx="12" cy="12" r="9"/><path d="M3 12h18M12 3c3 3 3 15 0 18M12 3c-3 3-3 15 0 18"/></svg>Velunora.srl</span>
    </div>
    <div class="line contact" style="top:127px;font-size:9px">
      <span class="contact-item"><span class="icon-at">@</span>office@velunora.srl</span>
    </div>
  </section>

</main>
</body>
</html>
```